Harrow grounds and gardens

Lawn Maintenance, Spring Fall Clean Ups, Stone Walls & Walkways, Commercial and Residental Snow Removal carpentry and handyman services

Industry/Entity Type

Carpentry

Contact Information for Business Card

Harrow Grounds and Gardens 23 Brambleton Fern Rd Alderbrook NY 10988 555 310 2286 Cell 555412 9083

```html
<!DOCTYPE html>
<html lang="en">
<head>
<meta charset="utf-8">
<title>Harrow Grounds and Gardens – Business Card</title>
<link href="https://fonts.googleapis.com/css2?family=Ubuntu:wght@400;500;700&display=swap" rel="stylesheet">
<style>
  :root {
    --bg: #e9e7e2;
    --card-white: #ffffff;
    --green-light: #7cc35c;
    --green-mid: #5bb046;
    --green-deep: #3f9a3a;
    --brand-green: #58ab3f;
    --text-on-green: #ffffff;
    --divider: rgba(255,255,255,0.75);
  }
  * { box-sizing: border-box; margin: 0; padding: 0; }
  html, body {
    width: 1200px; height: 818px; overflow: hidden;
    background: var(--bg);
    font-family: "Ubuntu", sans-serif;
  }
  .stage {
    width: 1200px; height: 818px;
    display: flex; align-items: center; justify-content: center;
  }
  .business-card {
    width: 860px; height: 492px;
    background: var(--card-white);
    box-shadow: 0 14px 34px rgba(0,0,0,0.18);
    display: flex; flex-direction: column;
    overflow: hidden;
  }
  .brand-area {
    height: 212px;
    display: flex; align-items: center;
    padding-left: 120px;
    gap: 22px;
  }
  .brand-dot {
    width: 58px; height: 58px; border-radius: 50%;
    background: var(--brand-green);
    flex: none;
  }
  .brand-name {
    color: var(--brand-green);
    font-weight: 700;
    font-size: 52px;
    line-height: 1.02;
    letter-spacing: -0.5px;
  }
  .info-band {
    flex: 1;
    background: linear-gradient(180deg, var(--green-light) 0%, var(--green-mid) 55%, var(--green-deep) 100%);
    color: var(--text-on-green);
    display: flex;
    padding: 38px 56px 0 56px;
  }
  .contact {
    width: 340px;
    padding-right: 30px;
  }
  .employee-name {
    font-weight: 700;
    font-size: 33px;
    margin-bottom: 14px;
  }
  .phone-list { list-style: none; margin-bottom: 18px; }
  .phone-list li {
    display: flex; align-items: center; gap: 12px;
    font-size: 26px; line-height: 1.3;
  }
  .phone-icon { width: 22px; height: 22px; flex: none; }
  .address { font-size: 26px; line-height: 1.3; font-style: normal; }
  .divider {
    width: 2px; background: var(--divider);
    margin: 6px 34px 40px 0;
  }
  .services { list-style: none; font-size: 25px; line-height: 1.3; padding-top: 4px; }
</style>
</head>
<body>
<main class="stage">
  <article class="business-card">
    <header class="brand-area">
      <span class="brand-dot" aria-hidden="true"></span>
      <h1 class="brand-name">Harrow<br>Grounds and Gardens</h1>
    </header>
    <section class="info-band">
      <div class="contact">
        <h2 class="employee-name">Employee Name</h2>
        <ul class="phone-list">
          <li>555412 9083
            <svg class="phone-icon" viewBox="0 0 22 22" aria-label="office phone">
              <rect x="1" y="1" width="20" height="20" rx="2" fill="none" stroke="#fff" stroke-width="2"/>
              <rect x="6" y="5" width="10" height="4" fill="#fff"/>
              <rect x="6" y="11" width="10" height="6" fill="none" stroke="#fff" stroke-width="1.6"/>
            </svg>
          </li>
          <li>555 310 2286
            <svg class="phone-icon" viewBox="0 0 22 22" aria-label="cell phone">
              <rect x="1" y="1" width="20" height="20" rx="2" fill="none" stroke="#fff" stroke-width="2"/>
              <rect x="7" y="4" width="8" height="14" rx="1.5" fill="none" stroke="#fff" stroke-width="1.6"/>
              <circle cx="11" cy="15.5" r="1" fill="#fff"/>
            </svg>
          </li>
        </ul>
        <address class="address">23 Brambleton Fern Rd<br>Alderbrook NY 10988</address>
      </div>
      <div class="divider" aria-hidden="true"></div>
      <ul class="services">
        <li>Lawn Maintenance</li>
        <li>Spring Fall Clean Ups</li>
        <li>Stone Walls &amp; Walkways</li>
        <li>Commercial and Residental</li>
        <li>Snow Removal carpentry and</li>
        <li>handyman services</li>
      </ul>
    </section>
  </article>
</main>
</body>
</html>
```